gutter trailer wrap

I want to wrap my trailer for my gutter business. I want it to be flashy and have " seamless gutter and phone number very prominently displayed. My logo can be smaller on the wrap

I want also included " Licensed and Insured "

We install seamless gutters

Target Market(s)

home owners

Industry/Entity Type

Rain gutters - Seamless gutters

Colors
0054AA
0677BA
7BADD7
CADEEF
E8F1F8
59FF00
82FF00
B8FF75
E3FFCB
F4FFEA

Requirements
Must have
• vibrant colors

```html
<!DOCTYPE html>
<html lang="en">
<head>
<meta charset="utf-8">
<title>Seamless Gutters Trailer Wrap</title>
<link href="https://fonts.googleapis.com/css2?family=Archivo+Black&family=Montserrat:wght@800&display=swap" rel="stylesheet">
<style>
  :root {
    --bg: #ffffff;
    --blue-deep: #1a2a9c;
    --blue-bright: #0a63d8;
    --navy: #16105e;
    --red: #ea1c24;
    --yellow: #fff200;
    --white: #ffffff;
    --sky-light: #7fd3f2;
    --sky-deep: #1f6ec9;
    --gold: #d9a520;
    --badge-blue: #1c5ba8;
  }
  html, body {
    margin: 0;
    width: 1200px;
    height: 1200px;
    overflow: hidden;
    background: var(--bg);
  }
  .canvas {
    position: relative;
    width: 1200px;
    height: 1200px;
  }
  .wrap-side {
    position: absolute;
    left: 60px;
    top: 375px;
    width: 1080px;
    height: 450px;
  }
  .headline { font-family: "Archivo Black", sans-serif; }
  .support { font-family: "Montserrat", sans-serif; font-weight: 800; }
</style>
</head>
<body>
<main class="canvas">
  <svg class="wrap-side" viewBox="0 0 1080 450" xmlns="http://www.w3.org/2000/svg">
    <defs>
      <linearGradient id="blue-field" x1="0" y1="0" x2="1" y2="1">
        <stop offset="0" stop-color="var(--blue-deep)"/>
        <stop offset="0.55" stop-color="var(--blue-bright)"/>
        <stop offset="1" stop-color="var(--blue-deep)"/>
      </linearGradient>
      <linearGradient id="photo-tone" x1="0" y1="0" x2="1" y2="1">
        <stop offset="0" stop-color="var(--sky-light)"/>
        <stop offset="1" stop-color="var(--sky-deep)"/>
      </linearGradient>
    </defs>

    <!-- base field -->
    <rect class="blue-field" width="940" height="450" fill="url(#blue-field)"/>

    <!-- house photo area -->
    <polygon class="gutter-photo" role="img" aria-label="Photo of a blue house with white seamless gutter and downspout"
      points="586,0 940,0 940,255 560,345" fill="url(#photo-tone)"/>

    <!-- red accents -->
    <polygon class="red-corner" points="0,245 178,450 0,450" fill="var(--red)"/>
    <polygon class="red-band" points="560,345 940,255 940,450 500,450" fill="var(--red)"/>

    <!-- front navy panel -->
    <rect class="front-panel" x="940" y="0" width="140" height="450" fill="var(--navy)"/>

    <!-- headline group, all on one slant -->
    <g class="headline-block" transform="rotate(-16 60 220)">
      <text class="support" x="52" y="165" font-size="28" fill="var(--white)" textLength="240" lengthAdjust="spacingAndGlyphs">TOP QUALITY</text>
      <text class="headline" x="60" y="226" font-size="62" fill="var(--yellow)" textLength="420" lengthAdjust="spacingAndGlyphs">SEAMLESS</text>
      <text class="headline" x="70" y="294" font-size="70" fill="var(--white)" textLength="400" lengthAdjust="spacingAndGlyphs">GUTTERS</text>
      <text class="headline" x="300" y="330" font-size="22" fill="var(--red)" textLength="160" lengthAdjust="spacingAndGlyphs">CALL NOW...!</text>
      <text class="headline" x="200" y="378" font-size="38" fill="var(--yellow)" textLength="350" lengthAdjust="spacingAndGlyphs">(555)-014-2290</text>
      <text class="support" x="250" y="402" font-size="13" fill="var(--white)" letter-spacing="1.5" textLength="260" lengthAdjust="spacingAndGlyphs">BEST QUALITY - FAST SERVICE</text>
    </g>

    <text class="support" x="55" y="385" font-size="28" fill="var(--white)">FREE</text>
    <text class="support" x="55" y="410" font-size="19" fill="var(--white)">ESTIMATES</text>

    <!-- certification badges -->
    <circle class="seal-badge" cx="497" cy="353" r="30" fill="var(--gold)"/>
    <rect class="rating-badge" x="470" y="390" width="55" height="35" rx="3" fill="var(--badge-blue)"/>

    <!-- company name -->
    <rect class="brand-mark" x="602" y="258" width="14" height="14" fill="var(--red)"/>
    <text class="headline" x="622" y="271" font-size="14" fill="var(--red)">LARKFIELD</text>
    <text class="headline" x="622" y="282" font-size="7" fill="var(--red)">CONSTRUCTION &amp; ROOFING</text>
  </svg>
</main>
</body>
</html>
```